Local Roofing Company Billboard Design

We need a billboard design for an 8' x 32' billboard. This billboard would need to be easily readable and stand out well.
I have uploaded a design that we like - simple, readable, and gets the point across. We do NOT want the $1000 off offer included.
We are looking for a black background with white copy so it will stand out. We want the following on the billboard:
Kessler Roofing logo
kessler-roofing.example (optional)
555.271.6384 (mandatory)
Photo is optional, depends on how it all lays out
Production file must comply with layout requirements (uploaded).
Target Market(s)
Homeowners
Font styles to use
Other font styles liked:
- match font from logo
Colors
Designer to choose colors to be used in the design.
Requirements
Must have
- Black background, white copy, logo must be large and legible. Colors used must match our logo colors.

```html
<!DOCTYPE html>
<html lang="en">
<head>
<meta charset="utf-8">
<title>Kessler Roofing Billboard</title>
<link rel="stylesheet" href="https://fonts.googleapis.com/css2?family=Montserrat:wght@600;700&display=swap">
<style>
  :root {
    --stage: #8d8e92;
    --board-black: #060606;
    --brand-orange: #e85a26;
    --badge-navy: #26348a;
    --white: #ffffff;
    --photo-sky: #c9c6bf;
    --photo-roof: #6b6a6c;
    --photo-warm: #8a6a4c;
    --photo-deep: #3b3a36;
  }
  * { box-sizing: border-box; margin: 0; padding: 0; }
  html, body {
    width: 1200px;
    height: 699px;
    overflow: hidden;
    background: var(--stage);
    font-family: "Montserrat", sans-serif;
  }
  .billboard {
    position: absolute;
    left: 40px;
    top: 197px;
    width: 1120px;
    height: 305px;
    background: var(--board-black);
    overflow: hidden;
  }
  .billboard__shapes {
    position: absolute;
    inset: 0;
    width: 100%;
    height: 100%;
  }
  .billboard__photo {
    position: absolute;
    inset: 0;
    background: linear-gradient(160deg, var(--photo-sky) 0%, var(--photo-roof) 28%, var(--photo-warm) 55%, var(--photo-deep) 100%);
    clip-path: polygon(74.5% 0, 100% 0, 100% 100%, 67.7% 100%, 84.9% 37.2%);
  }
  .brand {
    position: absolute;
    left: 38px;
    top: 92px;
    display: flex;
    align-items: center;
    gap: 12px;
  }
  .brand__mark {
    width: 26px;
    height: 26px;
    background: var(--brand-orange);
  }
  .brand__name {
    color: var(--white);
    font-weight: 700;
    font-size: 30px;
    line-height: 1;
    white-space: nowrap;
  }
  .tagline {
    position: absolute;
    left: 38px;
    top: 170px;
    color: var(--white);
    font-weight: 600;
    font-size: 32px;
    line-height: 35px;
    white-space: nowrap;
  }
  .tagline .accent { color: var(--brand-orange); }
  .divider {
    position: absolute;
    left: 316px;
    top: 174px;
    width: 2px;
    height: 97px;
    background: var(--brand-orange);
  }
  .contact__web {
    position: absolute;
    left: 351px;
    top: 173px;
    color: var(--white);
    font-weight: 700;
    font-size: 21px;
    line-height: 1;
    white-space: nowrap;
  }
  .contact__phone {
    position: absolute;
    left: 349px;
    top: 218px;
    color: var(--white);
    font-weight: 700;
    font-size: 55px;
    line-height: 1;
    letter-spacing: -0.5px;
    white-space: nowrap;
  }
</style>
</head>
<body>
  <div class="billboard">
    <div class="billboard__photo" role="img" aria-label="Photo of two roofers reviewing plans in front of a shingled house"></div>
    <svg class="billboard__shapes" viewBox="0 0 2114 576" preserveAspectRatio="none" aria-hidden="true">
      <polygon class="accent-panel" points="996,0 1554,0 1772,214 1497,494" fill="var(--brand-orange)"/>
      <polygon class="partner-badge" points="1507,36 1690,220 1507,404 1324,220" fill="var(--badge-navy)"/>
    </svg>

    <div class="brand">
      <span class="brand__mark"></span>
      <span class="brand__name">Kessler Roofing</span>
    </div>

    <p class="tagline">
      <span class="accent">Installing</span><br>
      quality roofs<br>
      across <span class="accent">Arizona</span>
    </p>

    <div class="divider"></div>

    <p class="contact__web">www.kessler-roofing.example</p>
    <p class="contact__phone">555.271.6384</p>
  </div>
</body>
</html>
```